New company business cards with new company logo

We need a new business card designed as we have a new company logo and are going for a more 'flat design' look. Our company name is Veloristat and we are a global data focused Clinical Research Organisation. We'd ideally like one side with room for the individuals contact details, our full logo and our services - and one side which is quite plain, for example perhaps using the green triangular image attached with just the white 'V' in the center (also attached).

Industry/Entity Type

Business

Requirements
Must have
• Our main colour: #42b5a9
Please make text dark grey: #373737

```html
<!DOCTYPE html>
<html lang="en">
<head>
<meta charset="utf-8">
<title>Veloristat Business Card</title>
<link rel="stylesheet" href="https://fonts.googleapis.com/css2?family=Open+Sans:wght@400;600;700&display=swap">
<style>
  :root {
    --brand: #42b5a9;
    --brand-deep: #2e9c91;
    --brand-mist: #e3f1ef;
    --ink: #373737;
    --night: #2a2a2c;
    --paper: #ffffff;
    --backdrop: #ececec;
  }
  * { box-sizing: border-box; margin: 0; padding: 0; }
  html, body { width: 1200px; height: 726px; overflow: hidden; }
  body {
    background: var(--backdrop);
    font-family: "Open Sans", Arial, sans-serif;
    color: var(--ink);
    position: relative;
  }
  .card {
    position: absolute;
    top: 208px;
    width: 540px;
    height: 309px;
    overflow: hidden;
    box-shadow: 0 6px 18px rgba(0,0,0,0.12);
  }
  .card-back { left: 40px; }
  .card-front { left: 620px; background: var(--paper); }

  .back-field {
    position: absolute; inset: 0;
    background: linear-gradient(135deg, #8fcfc7 0%, #7cc0b8 45%, #86c9c1 70%, #74b8af 100%);
  }
  .back-emblem {
    position: absolute;
    left: 50%; top: 50%;
    width: 150px; height: 150px;
    margin: -75px 0 0 -75px;
    border-radius: 50%;
    background: var(--paper);
    display: flex; align-items: center; justify-content: center;
  }
  .back-emblem .brand-name { font-size: 22px; font-weight: 600; color: var(--brand); }

  .front-halo {
    position: absolute;
    right: -20px; top: -70px;
    width: 250px; height: 250px;
    border-radius: 50%;
    background: var(--brand-mist);
  }
  .front-swoosh { position: absolute; left: 0; top: 0; width: 540px; height: 309px; }

  .holder { position: absolute; left: 36px; top: 96px; }
  .holder-name { font-size: 16px; font-weight: 700; color: var(--brand); }
  .holder-role { font-size: 10px; color: var(--ink); margin-top: 1px; }

  .contact-list {
    position: absolute; left: 30px; top: 196px;
    list-style: none; font-size: 12px; line-height: 17px;
  }
  .contact-list li { display: flex; align-items: center; gap: 7px; }
  .contact-list svg { width: 11px; height: 11px; fill: var(--brand); flex: none; }
  .contact-list .accent { color: var(--brand); }
  .contact-list .fax { margin-left: 6px; }

  .brand-lockup {
    position: absolute; left: 360px; top: 100px;
    display: flex; align-items: center; gap: 8px;
  }
  .brand-dot { width: 44px; height: 44px; border-radius: 50%; background: var(--brand-deep); flex: none; }
  .brand-text .brand-name { font-size: 23px; font-weight: 400; color: var(--night); line-height: 1; }
  .brand-tagline {
    font-size: 8.5px; color: var(--ink);
    border-top: 1px solid var(--night);
    margin-top: 3px; padding-top: 1px; letter-spacing: 0.3px;
    white-space: nowrap;
  }
</style>
</head>
<body>

<section class="card card-back">
  <div class="back-field" role="img" aria-label="Faceted teal triangle pattern background"></div>
  <div class="back-emblem"><span class="brand-name">Veloristat</span></div>
</section>

<section class="card card-front">
  <div class="front-halo"></div>

  <svg class="front-swoosh" viewBox="0 0 540 309" aria-hidden="true">
    <path d="M230 309 C350 285 460 230 540 178 L540 309 Z" fill="var(--brand-deep)"/>
    <path d="M200 309 C340 292 460 248 540 212 L540 309 Z" fill="var(--paper)"/>
    <path d="M110 309 C290 296 440 258 540 230 L540 309 Z" fill="var(--night)"/>
    <path d="M150 309 C310 298 450 266 540 244 L540 309 Z" fill="var(--paper)"/>
    <path d="M130 309 C300 302 450 278 540 262 L540 309 Z" fill="var(--brand-deep)"/>
    <path d="M170 309 C320 305 460 290 540 282 L540 309 Z" fill="var(--paper)"/>
  </svg>

  <div class="holder">
    <p class="holder-name">Your Long Name</p>
    <p class="holder-role">Managing Director</p>
  </div>

  <ul class="contact-list">
    <li><svg viewBox="0 0 12 12"><path d="M6 0a4 4 0 0 0-4 4c0 3 4 8 4 8s4-5 4-8a4 4 0 0 0-4-4zm0 5.5A1.5 1.5 0 1 1 6 2.5a1.5 1.5 0 0 1 0 3z"/></svg><span>Your Commercial or office address</span></li>
    <li><svg viewBox="0 0 12 12"><path d="M2 1h3l1 3-2 1a7 7 0 0 0 3 3l1-2 3 1v3c-6 0-9-4-9-9z"/></svg><span>00.00.00.0000</span><svg class="fax" viewBox="0 0 12 12"><path d="M3 0h6v3H3zM1 4h10v6H9v2H3v-2H1zm3 4v3h4V8z"/></svg><span>00.00.00.0000</span></li>
    <li><svg viewBox="0 0 12 12"><path d="M0 2h12v8H0zm1 1 5 4 5-4z"/></svg><span>yourname@veloristat.com</span></li>
    <li><svg viewBox="0 0 12 12"><circle cx="6" cy="6" r="5.5"/></svg><span>www.<span class="accent">veloristat</span>.com</span></li>
  </ul>

  <div class="brand-lockup">
    <span class="brand-dot"></span>
    <div class="brand-text">
      <p class="brand-name">Veloristat</p>
      <p class="brand-tagline">Clarity In Every Dataset</p>
    </div>
  </div>
</section>

</body>
</html>
```